Norvane Medical Business Card Design

This is a private medical device company. We recently launched the new website and would like to redesign the business cards. Please see the website: www.norvanemedical-demo.com. We'd like to keep the cards simple and professional but modern to match the website and collateral branding. Our customers are physicians and investors. I have attached the old design for comparison. I have also attached the updated logo. Please note the business card information will change, based on all employees who need to order them. So I will need to be able easily edit the copy.
Updates

Hi designers-thank you very much for submitting designs. I look forward to the results!! Jodi

Target Market(s)

Our target audience are physicians

Industry/Entity Type

Medical

Contact Information for Business Card

Denise Halvorsen
Director of Marketing and Reimbursement
dhalvorsen@norvanemedical-demo.com
M: xxx-xxx-xxxx
O: xxx-xxx-xxxx
4120 Lark Mill Rd.
Suite 380
Austin, TX 78759

Font styles to use
Sans Serif

Requirements
Must have
• Must include the logo and a color or color from the logo and branding
Nice to have
• Maybe include the logo icon on the back.

```html
<!DOCTYPE html>
<html lang="en">
<head>
<meta charset="utf-8">
<title>Norvane Medical – Business Card</title>
<link href="https://fonts.googleapis.com/css2?family=Open+Sans:wght@300;400;700&display=swap" rel="stylesheet">
<style>
  :root {
    --stage: #e9e9e7;
    --card-white: #ffffff;
    --teal: #6fbfca;
    --teal-light: #9ad3db;
    --teal-deep: #58aebb;
    --ink: #3d3b3c;
    --on-teal: #ffffff;
    --address: #4f7f88;
  }
  * { box-sizing: border-box; margin: 0; padding: 0; }
  html, body {
    width: 1200px; height: 1023px; overflow: hidden;
    background: var(--stage);
    font-family: "Open Sans", Arial, sans-serif;
  }
  .stage {
    position: relative; width: 1200px; height: 1023px;
    display: flex; align-items: center; justify-content: center; gap: 40px;
  }
  .card {
    position: relative; width: 520px; height: 297px;
    background: var(--card-white);
    box-shadow: 0 6px 18px rgba(0,0,0,.18);
    overflow: hidden;
  }
  .card-art { position: absolute; inset: 0; width: 100%; height: 100%; }

  /* Front */
  .wordmark {
    position: absolute; display: flex; align-items: center; gap: 10px;
    color: var(--ink); font-weight: 400; white-space: nowrap;
  }
  .wordmark .mark-square { width: 20px; height: 20px; background: var(--teal); flex: none; }
  .front .wordmark { left: 22px; top: 96px; font-size: 22px; }

  .contact {
    position: absolute; right: 22px; top: 58px; text-align: right;
    color: var(--on-teal);
  }
  .contact .name {
    font-weight: 700; font-size: 17px; letter-spacing: .5px;
    text-transform: uppercase; color: var(--ink);
  }
  .contact .title { font-size: 11px; margin-top: 2px; }
  .contact .phones { margin-top: 22px; font-size: 10.5px; font-weight: 300; line-height: 1.55; }
  .contact .phone-line { display: flex; justify-content: flex-end; align-items: center; gap: 8px; }
  .contact .phone-line svg { width: 10px; height: 10px; }
  .contact .email { margin-top: 8px; font-size: 10.5px; font-weight: 300; }

  .address {
    position: absolute; left: 22px; bottom: 20px;
    color: var(--address); font-size: 11px; font-weight: 400;
    letter-spacing: .6px; line-height: 1.45; text-transform: uppercase;
  }

  /* Back */
  .back .wordmark { left: 50%; top: 50%; transform: translate(-50%, -50%); font-size: 30px; }
  .back .wordmark .mark-square { width: 26px; height: 26px; }
</style>
</head>
<body>
<main class="stage">

  <section class="card front" aria-label="Business card front">
    <svg class="card-art" viewBox="0 0 520 297" preserveAspectRatio="none" aria-hidden="true">
      <rect width="520" height="297" fill="var(--teal)"/>
      <polygon points="300,205 520,190 520,297 340,297" fill="var(--teal-deep)" opacity=".35"/>
      <polygon points="0,170 290,205 0,297" fill="var(--teal-light)" opacity=".55"/>
      <polygon points="175,0 290,205 330,0" fill="var(--teal-light)" opacity=".35"/>
      <polygon points="0,0 175,0 290,205 0,170" fill="var(--card-white)"/>
    </svg>

    <div class="wordmark"><span class="mark-square"></span>Norvane Medical</div>

    <div class="contact">
      <p class="name">Denise Halvorsen</p>
      <p class="title">Director of Marketing and Reimbursement</p>
      <div class="phones">
        <p class="phone-line">xxx-xxx-xxxx
          <svg viewBox="0 0 10 10" aria-hidden="true"><rect x="2.5" y="0.5" width="5" height="9" rx="1" fill="none" stroke="currentColor"/></svg>
        </p>
        <p class="phone-line">xxx-xxx-xxxx
          <svg viewBox="0 0 10 10" aria-hidden="true"><path d="M2 1h2l1 2.5-1.3 1a6 6 0 0 0 2.8 2.8l1-1.3L9 7v2a1 1 0 0 1-1 1A8 8 0 0 1 0 2a1 1 0 0 1 1-1z" fill="currentColor"/></svg>
        </p>
      </div>
      <p class="email">dhalvorsen@norvanemedical-demo.com</p>
    </div>

    <p class="address">4120 Lark Mill Rd.<br>Suite 380 Austin, TX 78759</p>
  </section>

  <section class="card back" aria-label="Business card back">
    <div class="wordmark"><span class="mark-square"></span>Norvane Medical</div>
  </section>

</main>
</body>
</html>
```